R&T Photography (business cards)

Business cards for a photography business. We also photographs events, portraits, headshots.
Colors: Vanilla w/ dark blue (not Aqua or Navy)
Website: randtphotography482-mailbox.net
Email: randtphotography76@mailbox.net
Company Name: R&T Photography
Letter style/font for company name is French Script
We would like a card that somehow delivers a combination of softness, confidence and strength.

Target Market(s)

Wedding clients

Industry/Entity Type

Business

Font styles to use
Decorative
Script

Colors
0d5ba7
3176b5
5c5c5c
dbdbdb

Requirements
Must have
• Bold and/or raised print for company name. Website should also stand out. Telephone contact numbers are:
• (555) 214-7730
• (555) 862-3046
• Website: RandTPhotohraphy482-mailbox.net
• Business address: PO Box 6204, Orlando, FL 32899
• Back of card should state: referrals are welcome.
Nice to have
• some lace/scroll
Should not have
• Non-metallic.

```html
<!DOCTYPE html>
<html lang="en">
<head>
<meta charset="utf-8">
<title>R&amp;T Photography — Business Cards</title>
<link href="https://fonts.googleapis.com/css2?family=Arimo:wght@400;700&family=Tinos:wght@400&display=swap" rel="stylesheet">
<style>
  :root {
    --backdrop: #ecebe7;
    --brand-blue: #1a5ba6;
    --brand-blue-light: #3176b5;
    --card-white: #ffffff;
    --text-grey: #5c5c5c;
    --wreath-grey: #dbdbdb;
    --faint-blue: #2a67b0;
    --faint-text: #3a73b6;
  }
  * { box-sizing: border-box; margin: 0; padding: 0; }
  html, body {
    width: 1200px;
    height: 915px;
    overflow: hidden;
    background: var(--backdrop);
  }
  .card-set {
    position: relative;
    width: 1200px;
    height: 915px;
  }
  .card {
    position: absolute;
    top: 112px;
    width: 440px;
    height: 690px;
    border-radius: 32px;
    overflow: hidden;
    box-shadow: 0 6px 18px rgba(0,0,0,0.18);
  }

  /* Back of card */
  .card-back {
    left: 140px;
    background: var(--brand-blue);
  }
  .card-back .wreath-area {
    position: absolute;
    left: 50px;
    top: 200px;
    width: 340px;
    height: 250px;
    border-radius: 50%;
    background: radial-gradient(ellipse at center, var(--brand-blue) 58%, var(--faint-blue) 70%, var(--brand-blue) 82%);
  }
  .card-back .brand-name {
    position: absolute;
    left: 0;
    right: 0;
    top: 300px;
    text-align: center;
    font-family: "Arimo", Arial, sans-serif;
    font-weight: 700;
    font-size: 34px;
    color: var(--faint-text);
  }
  .card-back .referral-note {
    position: absolute;
    left: 0;
    right: 0;
    top: 565px;
    text-align: center;
    font-family: "Tinos", "Times New Roman", serif;
    font-size: 22px;
    letter-spacing: 0.6px;
    color: var(--card-white);
  }

  /* Front of card */
  .card-front {
    left: 620px;
    background: var(--card-white);
  }
  .card-front .wreath-area {
    position: absolute;
    left: 45px;
    top: 70px;
    width: 350px;
    height: 265px;
    border-radius: 50%;
    background: radial-gradient(ellipse at center, var(--card-white) 60%, var(--wreath-grey) 72%, var(--card-white) 84%);
  }
  .card-front .brand-name {
    position: absolute;
    left: 0;
    right: 0;
    top: 178px;
    text-align: center;
    font-family: "Arimo", Arial, sans-serif;
    font-weight: 700;
    font-size: 36px;
    color: var(--brand-blue);
  }
  .contact-list {
    position: absolute;
    left: 46px;
    top: 408px;
    list-style: none;
  }
  .contact-item {
    display: flex;
    align-items: center;
    height: 36px;
    font-family: "Arimo", Arial, sans-serif;
    font-size: 19px;
    color: var(--text-grey);
  }
  .contact-icon {
    width: 22px;
    height: 22px;
    margin-right: 14px;
    flex: none;
  }
  .website-band {
    position: absolute;
    left: 0;
    right: 0;
    bottom: 0;
    height: 90px;
    background: var(--brand-blue);
    display: flex;
    align-items: center;
    padding-left: 30px;
    font-family: "Arimo", Arial, sans-serif;
    font-size: 19px;
    color: var(--card-white);
  }
  .website-band .contact-icon { margin-right: 8px; }
</style>
</head>
<body>
<main class="card-set">

  <section class="card card-back" aria-label="Back of business card">
    <div class="wreath-area" role="img" aria-label="Faint leafy wreath ornament framing the company name"></div>
    <div class="brand-name">R&amp;T Photography</div>
    <p class="referral-note">Referrals are welcome</p>
  </section>

  <section class="card card-front" aria-label="Front of business card">
    <div class="wreath-area" role="img" aria-label="Grey leafy wreath ornament framing the company name"></div>
    <h1 class="brand-name">R&amp;T Photography</h1>

    <ul class="contact-list">
      <li class="contact-item">
        <svg class="contact-icon" viewBox="0 0 22 22" aria-hidden="true">
          <rect width="22" height="22" rx="4" fill="var(--brand-blue)"/>
          <path d="M11 4a5 5 0 0 0-5 5c0 3.6 5 9 5 9s5-5.4 5-9a5 5 0 0 0-5-5z" fill="#fff"/>
          <circle cx="11" cy="9" r="2" fill="var(--brand-blue)"/>
        </svg>
        PO Box 6204, Orlando, FL 32899
      </li>
      <li class="contact-item">
        <svg class="contact-icon" viewBox="0 0 22 22" aria-hidden="true">
          <rect width="22" height="22" rx="4" fill="var(--brand-blue)"/>
          <rect x="6.5" y="3.5" width="9" height="15" rx="1.5" fill="none" stroke="#fff" stroke-width="1.6"/>
          <rect x="8.5" y="6" width="5" height="4" fill="#fff"/>
          <circle cx="11" cy="15.5" r="1" fill="#fff"/>
        </svg>
        (555) 214-7730
      </li>
      <li class="contact-item">
        <svg class="contact-icon" viewBox="0 0 22 22" aria-hidden="true">
          <rect width="22" height="22" rx="4" fill="var(--brand-blue)"/>
          <path d="M7 5l2.5-.5 1.5 3.5-1.7 1.2a8 8 0 0 0 3.5 3.5l1.2-1.7 3.5 1.5-.5 2.5c-.3 1-1.3 1.5-2.3 1.3C9.5 16 6 12.5 5.2 7.3 5 6.3 5.8 5.3 7 5z" fill="#fff"/>
        </svg>
        (555) 862-3046
      </li>
      <li class="contact-item">
        <svg class="contact-icon" viewBox="0 0 22 22" aria-hidden="true">
          <rect width="22" height="22" rx="4" fill="var(--brand-blue)"/>
          <rect x="4" y="6.5" width="14" height="9.5" fill="none" stroke="#fff" stroke-width="1.5"/>
          <path d="M4 6.5l7 5.5 7-5.5" fill="none" stroke="#fff" stroke-width="1.5"/>
        </svg>
        randtphotography76@mailbox.net
      </li>
    </ul>

    <div class="website-band">
      <svg class="contact-icon" viewBox="0 0 22 22" aria-hidden="true">
        <g fill="none" stroke="#fff" stroke-width="1.5">
          <circle cx="11" cy="11" r="8.5"/>
          <ellipse cx="11" cy="11" rx="3.8" ry="8.5"/>
          <path d="M2.5 11h17M4 6.5h14M4 15.5h14"/>
        </g>
      </svg>
      www. randtphotography482-mailbox.net
    </div>
  </section>

</main>
</body>
</html>
```